Therapy Dog Business need a brochure

I need a brochure designed for my Canine Assisted Therapy business in Victoria Australia. I have a logo already and info and photos to upload.
Best as white background and using the colours from the logo please
Updates

Hi Everyone,
I am sorry to have to revise the brief. I have added three new photos I was unable to add due to the size. I have had to wait for my photographer to change the size to add them today. I have been really inspired by all the work you have done so far. Thank you.
Could you please add the following on the brochure. (Under the individual dogs photo)
1. Juniper is the white dog. Please add the following under her picture. Juniper is one of the first Court Dogs in Australia. Working in Victoria, she has worked in the following Courts. The Ostrander Inquest Bench, The Dunmore Justice Hall in Collingwood, and the Brackwell Tribunal in Melbourne CBD. Her ability to use her intuition for clients is inspiring. Please contact us for potential use in Courts. Juniper has worked at the Harrowgate Safety College, and at STAVE at Har Saf. She is a stunning dog!
2. Barnaby is the golden dog. Barnaby is Junipers son, and had her instinct of intuition of who needs his help. Barnaby has an incredible soft approach as does his mother Juniper. He is incredibly safe with young children, and yet has a playful nature for adolescents and adults alike. He is soft and caring, and like his mother will go to those who need him most. Barnaby like his mother has worked at Harrowgate Safety, his time at HS included the Harrowgate Safety Council (HSC) Both he and his mother have very impressive CV'S!
3. Pepper the black dog. Pepper is my Therapy and Assistance dog "trainer" she is safe and stable with all the dogs and people I train for Therapy Dog Training and Assistance Dog Training. She has also been with me on my journey as a Counsellor and I have been able to work alongside her and Juniper for Counselling sessions.
She is soft, caring, and also intuitive. I am incredibly grateful for her help, as well as Juniper and Barnaby.
ALSO I am so sorry to add this but could you also add the following: Maybe in dot point?
Court Dog Availability
Therapy Dog Visits - Lawyers - Courts - Child Protection
Police Station / Ambulance Station / Fire Station - Visits
Private Therapy Dog Sessions
website and email confirmation coming soon. Thank you

3. Pepper the black dog.

Target Market(s)

First Responders

Requirements
Must have
• All the photos provided.
Should not have
• Generic photos

```html
<!DOCTYPE html>
<html lang="en">
<head>
<meta charset="utf-8">
<title>Gentle Paw – Canine Assisted Therapy Brochure</title>
<link href="https://fonts.googleapis.com/css2?family=Anton&family=Figtree:ital,wght@0,400;0,500;0,600;0,700;0,800;1,700;1,800&family=Dancing+Script:wght@700&display=swap" rel="stylesheet">
<style>
  :root{
    --backdrop:#3b3b3d;
    --paper:#ffffff;
    --maroon:#7a2a3e;
    --maroon-deep:#5e1f31;
    --rose:#e07a80;
    --rose-soft:#f2b4b0;
    --orange:#f08a3c;
    --amber:#f5a94a;
    --brick:#b4442f;
    --ink:#3d3033;
    --muted:#6f6466;
    --sofa:#7f96d6;
    --white:#ffffff;
  }
  *{box-sizing:border-box;margin:0;padding:0}
  html,body{width:1200px;height:800px;overflow:hidden}
  body{background:var(--backdrop);font-family:"Figtree",sans-serif;color:var(--ink);position:relative}

  .page{position:absolute;top:116px;width:400px;height:568px;background:var(--paper);overflow:hidden}
  .page--back{left:190px}
  .page--front{left:610px}

  /* ---------- back page ---------- */
  .photo-circle{position:absolute;border-radius:50%;background:radial-gradient(circle at 45% 40%,#e9d6b5 0 22%,#8ea2dc 45%,#6f84c8 100%);border:3px solid var(--white)}
  .photo-circle--juniper{left:268px;top:-22px;width:124px;height:124px;background:radial-gradient(circle at 55% 40%,#efe3c8 0 24%,#8ea2dc 48%,#6f84c8 100%)}
  .photo-circle--pepper{left:245px;top:86px;width:112px;height:112px;background:radial-gradient(circle at 50% 55%,#2b2626 0 24%,#c8704e 46%,#8ea2dc 70%)}
  .photo-circle--barnaby{left:306px;top:177px;width:112px;height:112px;background:radial-gradient(circle at 50% 45%,#e4c48f 0 24%,#e3714f 45%,#8ea2dc 70%)}

  .dog{position:absolute;left:14px;width:250px}
  .dog--juniper{top:14px}
  .dog--pepper{top:95px;width:228px}
  .dog--barnaby{top:175px;width:270px}
  .dog__title{display:flex;align-items:center;gap:6px;font-size:9.6px;font-weight:700;color:var(--ink);margin-bottom:4px}
  .badge{width:19px;height:19px;border-radius:50%;background:var(--rose);border:2px solid var(--rose-soft);display:grid;place-items:center;flex:none}
  .badge::after{content:"";width:7px;height:6px;border-radius:50% 50% 45% 45%;background:var(--white)}
  .dog__text{font-size:6.6px;line-height:8.8px;color:var(--muted)}

  .services{position:absolute;left:0;top:256px;width:242px}
  .services__pill{display:inline-block;margin-left:14px;padding:1px 7px;border-radius:8px;background:linear-gradient(90deg,var(--brick),var(--amber));color:var(--white);font-size:7.6px;font-weight:600}
  .services__row{padding:3px 0 3px 13px;border-bottom:1px solid #cfc6c6;font-size:7.6px;color:var(--muted)}
  .services__row strong{color:var(--ink);font-weight:700}
  .services__row .dot{color:var(--orange)}

  .why{position:absolute;left:0;top:320px;width:400px;height:180px}
  .why__heading{position:absolute;left:15px;top:8px;font-size:16.4px;font-weight:800;color:var(--amber)}
  .why__cols{position:absolute;left:8px;top:36px;width:392px;display:flex;justify-content:space-between}
  .why__col{width:118px;text-align:center;color:var(--white)}
  .why__icon{width:29px;height:29px;margin:0 auto 5px;border-radius:50%;background:var(--orange);display:grid;place-items:center}
  .why__title{font-size:8.8px;font-weight:700;line-height:9.6px;margin-bottom:4px}
  .why__text{font-size:7px;line-height:8.8px;color:#f6e4e4}

  .join{position:absolute;left:208px;top:464px;width:192px;height:78px;border-radius:38px 0 0 0;background:linear-gradient(90deg,var(--orange),var(--amber));padding:7px 6px 0 18px;text-align:right;color:var(--white)}
  .join__title{font-size:9px;font-weight:800;font-style:italic;margin-bottom:2px}
  .join__text{font-size:6.2px;line-height:8.2px}

  .phone{position:absolute;display:flex;align-items:center;gap:6px;font-weight:800;font-style:italic}
  .phone--back{left:21px;top:516px;font-size:21px;color:var(--maroon)}
  .web--back{position:absolute;left:21px;top:546px;font-size:11.6px;font-weight:700;font-style:italic;color:var(--maroon)}

  /* ---------- front page ---------- */
  .hero{position:absolute;left:0;top:0;width:400px;height:270px}
  .hero__kicker{position:absolute;left:20px;top:16px;color:var(--white);font-size:12.8px;font-weight:700;font-style:italic}
  .hero__title{position:absolute;left:19px;top:30px;color:var(--white);font-family:"Anton",sans-serif;font-size:35px;line-height:40px;letter-spacing:.3px}
  .hero__script{position:absolute;left:22px;top:66px;color:var(--white);font-family:"Dancing Script",cursive;font-size:44px;line-height:46px}

  .brand{position:absolute;left:270px;top:18px;width:120px;height:120px;border-radius:50%;background:var(--white);display:grid;place-items:center}
  .brand__name{font-size:15px;font-weight:800;color:var(--maroon)}

  .about{position:absolute;left:224px;top:139px;width:180px;height:180px;border-radius:50%;background:radial-gradient(circle at 80% 45%,#f3b05a 0 18%,transparent 40%),linear-gradient(160deg,var(--orange),var(--brick) 65%,#c9362c);color:var(--white);text-align:center}
  .about__heading{position:absolute;left:6px;top:8px;width:144px;font-size:11.2px;font-weight:700;line-height:10.6px}
  .about__text{position:absolute;left:12px;top:44px;width:132px;font-size:6.9px;line-height:8.1px;font-weight:500}

  .dot-accent{position:absolute;border-radius:50%}
  .dot-accent--front{left:208px;top:258px;width:14px;height:14px;background:var(--amber)}
  .dot-accent--back{left:230px;top:93px;width:14px;height:14px;background:var(--rose)}
  .dot-accent--back2{left:375px;top:148px;width:12px;height:12px;background:#d98f3f}

  .benefits__heading{position:absolute;left:21px;top:266px;width:180px;padding-bottom:3px;border-bottom:1px solid #c9bdbd;font-size:16.4px;font-weight:700;line-height:17px;color:var(--orange)}
  .benefit{position:absolute;left:21px;width:366px}
  .benefit--comfort{top:318px}
  .benefit--stress{top:376px}
  .benefit--mental{top:434px}
  .benefit__title{display:flex;align-items:center;gap:6px;font-size:9.6px;font-weight:700;margin-bottom:3px}
  .benefit__text{font-size:7.2px;line-height:9.4px;color:var(--muted)}

  .phone--front{left:21px;top:530px;font-size:21px;color:var(--white)}
  .web--front{position:absolute;left:207px;top:527px;font-size:12.6px;line-height:16px;font-weight:700;font-style:italic;color:var(--white)}
</style>
</head>
<body>

<!-- Back page -->
<section class="page page--back" aria-label="Brochure back page">
  <div class="photo-circle photo-circle--juniper" role="img" aria-label="Photo of Juniper, the white dog, lying on a blue couch"></div>
  <div class="photo-circle photo-circle--pepper" role="img" aria-label="Photo of Pepper, the black dog, on a blue couch by a brick wall"></div>
  <div class="photo-circle photo-circle--barnaby" role="img" aria-label="Photo of Barnaby, the golden dog, lying on a blue couch"></div>
  <span class="dot-accent dot-accent--back"></span>
  <span class="dot-accent dot-accent--back2"></span>

  <article class="dog dog--juniper">
    <h3 class="dog__title"><span class="badge"></span>Juniper is the White Dog</h3>
    <p class="dog__text">Please add the following under her picture. Juniper is one of the first Court Dogs in Australia. Working in Victoria, she has worked in the following Courts. The Ostrander Inquest Bench, The Dunmore Justice Hall in Collingwood, and the Brackwell Tribunal in Melbourne CBD. Her ability to use her intuition for clients is inspiring. Please contact us for potential use in Courts. Juniper has worked at the Harrowgate Safety College, and at STAVE at Har Saf. She is a stunning dog!</p>
  </article>

  <article class="dog dog--pepper">
    <h3 class="dog__title"><span class="badge"></span>Pepper the Black Dog</h3>
    <p class="dog__text">Pepper is my Therapy and Assistance dog "trainer" she is safe and stable with all the dogs and people I train for Therapy Dog Training and Assistance Dog Training. She has also been with me on my journey as a Counsellor and I have been able to work alongside her and Juniper for Counselling sessions. She is soft, caring, and also intuitive. I am incredibly grateful for her help, as well as Juniper and Barnaby.</p>
  </article>

  <article class="dog dog--barnaby">
    <h3 class="dog__title"><span class="badge"></span>Barnaby is the Golden Dog</h3>
    <p class="dog__text">Barnaby is Junipers son, and had her instinct of intuition of who needs his help. Barnaby has an incredible soft approach as does his mother Juniper. He is incredibly safe with young children, and yet has a playful nature for adolescents and adults alike. He is soft and caring, and like his mother will go to those who need him most. Barnaby like his mother has worked at Harrowgate Safety, his time at HS included the Harrowgate Safety Council (HSC) Both he and his mother have very impressive CV'S!</p>
  </article>

  <div class="services">
    <span class="services__pill">Court Dog Availability</span>
    <p class="services__row"><strong>Therapy Dog Visits -</strong> Lawyers - Courts - Child Protection</p>
    <p class="services__row"><strong><span class="dot">•</span> Police Station <span class="dot">•</span> Ambulance Station <span class="dot">•</span> Fire Station</strong></p>
    <p class="services__row"><strong>Visits -</strong> Private Therapy Dog Sessions</p>
  </div>

  <svg width="400" height="200" viewBox="0 0 400 200" style="position:absolute;left:0;top:313px" aria-hidden="true">
    <defs>
      <linearGradient id="bandFill" x1="0" y1="0" x2="0" y2="1">
        <stop offset="0" stop-color="#6e2538"/><stop offset="1" stop-color="#8c3b47"/>
      </linearGradient>
    </defs>
    <path d="M0 14 Q7 4 14 14 T28 14 T42 14 T56 14 T70 14 T84 14 T98 14 T112 14 T126 14 T140 14 T154 14 T168 14 T182 14 T196 14 T210 14 T224 14 T238 14 T252 14 T266 14 T280 14 T294 14 T308 14 T322 14 T336 14 T350 14 T364 14 T378 14 T392 14 T406 14 V150 Q260 170 180 176 Q60 186 0 140 Z" fill="url(#bandFill)"/>
    <path d="M0 140 Q60 186 180 176 Q260 170 400 150 V160 Q260 182 180 188 Q60 198 0 156 Z" fill="#e07a80"/>
  </svg>

  <div class="why">
    <h2 class="why__heading">Why Choose Canine Assisted Therapy?</h2>
    <div class="why__cols">
      <div class="why__col">
        <div class="why__icon"><svg width="16" height="16" viewBox="0 0 24 24"><path d="M12 21s-8-5.3-8-11a4.5 4.5 0 0 1 8-2.8A4.5 4.5 0 0 1 20 10c0 5.7-8 11-8 11z" fill="#fff"/></svg></div>
        <h3 class="why__title">Proven<br>Effectiveness</h3>
        <p class="why__text">Studies and testimonials highlight the positive effects therapy dogs have on emotional, psychological and physical health.</p>
      </div>
      <div class="why__col">
        <div class="why__icon"><svg width="16" height="16" viewBox="0 0 24 24"><circle cx="12" cy="15" r="4.5" fill="#fff"/><circle cx="6" cy="9" r="2.2" fill="#fff"/><circle cx="10" cy="5.5" r="2.2" fill="#fff"/><circle cx="14" cy="5.5" r="2.2" fill="#fff"/><circle cx="18" cy="9" r="2.2" fill="#fff"/></svg></div>
        <h3 class="why__title">Non-Invasive<br>and Gentle</h3>
        <p class="why__text">Therapy dogs provide a natural and non-threatening way to engage with patients, making it accessible for individuals who may feel apprehensive about traditional therapy methods.</p>
      </div>
      <div class="why__col">
        <div class="why__icon"><svg width="16" height="16" viewBox="0 0 24 24"><path d="M12 2l8 3v6c0 5-3.5 9-8 11-4.5-2-8-6-8-11V5z" fill="#fff"/><path d="M8 12l3 3 5-6" stroke="#f08a3c" stroke-width="2.2" fill="none"/></svg></div>
        <h3 class="why__title">Safe and<br>Trustworthy</h3>
        <p class="why__text">All therapy dogs are carefully trained to work with professionals, ensuring that interactions are safe, beneficial, and appropriate for all individuals.</p>
      </div>
    </div>
  </div>

  <div class="join">
    <h3 class="join__title">Join the Healing Journey Today!</h3>
    <p class="join__text">Whether you are seeking emotional support or mental health improvement, Canine Assisted Therapy offers a unique and compassionate approach to healing. Connect with us today to learn more about how a therapy dog can help enhance your life and well-being.</p>
  </div>

  <p class="phone phone--back">
    <svg width="19" height="19" viewBox="0 0 24 24" aria-hidden="true"><circle cx="12" cy="12" r="10.5" fill="none" stroke="currentColor" stroke-width="1.8"/><path d="M8.5 6.5l2 2.5-1.2 1.5a7 7 0 0 0 4.2 4.2l1.5-1.2 2.5 2-1 1.8c-4.5 0-9-4.5-9-9z" fill="currentColor"/></svg>
    0400 217 964
  </p>
  <p class="web--back">www.gentlepawtherapy.com.au | info@gentlepawtherapy.com.au</p>
</section>

<!-- Front page -->
<section class="page page--front" aria-label="Brochure front page">
  <svg class="hero" viewBox="0 0 400 270" role="img" aria-label="Photo of three dogs, two golden and one black, resting on a blue couch in front of a brick wall">
    <defs>
      <linearGradient id="heroFill" x1="0" y1="0" x2="0" y2="1">
        <stop offset="0" stop-color="#8e3526"/>
        <stop offset=".42" stop-color="#b85a3c"/>
        <stop offset=".58" stop-color="#8b9ad4"/>
        <stop offset="1" stop-color="#6f86cf"/>
      </linearGradient>
    </defs>
    <path d="M0 0 H300 Q245 60 265 130 Q285 210 230 248 Q170 282 90 262 Q30 248 0 215 Z" fill="url(#heroFill)"/>
  </svg>
  <p class="hero__kicker">Discover the Healing Power of</p>
  <h1 class="hero__title">Canine-Assisted</h1>
  <p class="hero__script">Therapy</p>

  <div class="brand"><span class="brand__name">Gentle Paw</span></div>

  <div class="about">
    <h2 class="about__heading">What is<br>Canine Assisted<br>Therapy?</h2>
    <p class="about__text">Canine Assisted Therapy (CAT) is a unique form of therapy that integrates trained therapy dogs into the healing process. By working alongside licensed therapists, these compassionate and well-trained dogs help support individuals in overcoming emotional, physical, and psychological challenges. This innovative approach promotes healing, reduces stress, and enhances overall well-being.</p>
  </div>
  <span class="dot-accent dot-accent--front"></span>

  <h2 class="benefits__heading">Benefits of Canine Assisted Therapy.</h2>

  <article class="benefit benefit--comfort">
    <h3 class="benefit__title"><span class="badge"></span>Emotional Support and Comfort</h3>
    <p class="benefit__text">Therapy dogs provide immediate emotional support, offering comfort and companionship during therapy sessions. Their calming presence helps reduce feelings of anxiety, stress, and depression, and grief, creating a safe and nurturing environment for healing.</p>
  </article>
  <article class="benefit benefit--stress">
    <h3 class="benefit__title"><span class="badge"></span>Stress Relief and Relaxation</h3>
    <p class="benefit__text">Interacting with dogs has been proven to reduce cortisol (stress hormone) levels and increase serotonin and oxytocin, the “feel-good” hormones. This natural relief from stress makes Canine Assisted Therapy an ideal option for individuals dealing with anxiety, trauma, PTSD, and grief.</p>
  </article>
  <article class="benefit benefit--mental">
    <h3 class="benefit__title"><span class="badge"></span>Improved Mental Health</h3>
    <p class="benefit__text">Therapy dogs encourage social interaction, communication, and emotional expression, helping individuals address mental health challenges such as depression, anxiety, PTSD, and grief. The unconditional love and companionship of a dog can foster trust and openness during therapy sessions.</p>
  </article>

  <svg width="400" height="100" viewBox="0 0 400 100" style="position:absolute;left:0;top:468px" aria-hidden="true">
    <defs>
      <linearGradient id="footFill" x1="0" y1="0" x2="1" y2="0">
        <stop offset="0" stop-color="#c85a3e"/><stop offset="1" stop-color="#e07a80"/>
      </linearGradient>
    </defs>
    <path d="M0 44 Q120 8 230 26 Q330 42 400 0 V100 H0 Z" fill="#e99094"/>
    <path d="M0 54 Q120 20 230 36 Q330 52 400 12 V100 H0 Z" fill="url(#footFill)"/>
  </svg>

  <p class="phone phone--front">
    <svg width="19" height="19" viewBox="0 0 24 24" aria-hidden="true"><circle cx="12" cy="12" r="10.5" fill="none" stroke="currentColor" stroke-width="1.8"/><path d="M8.5 6.5l2 2.5-1.2 1.5a7 7 0 0 0 4.2 4.2l1.5-1.2 2.5 2-1 1.8c-4.5 0-9-4.5-9-9z" fill="currentColor"/></svg>
    0400 217 964
  </p>
  <p class="web--front">www.gentlepawtherapy.com.au<br>info@gentlepawtherapy.com.au</p>
</section>

</body>
</html>
```